Business Card Design Project

We are looking for a new business card design for a Drilling company in WA, Australia.

We are in between offices, however require a design in the meantime due to some upcoming events with our basic information.

The Logo for our company is Blue and Grey and would like this colour scheme throughout.

We are quite a new company so would like a memorable design that stands out and communicates a strong commitment to safety, quality of work and performance.

The company name is Ridgeback Boring Works (RBW)

The details to be included are as follows:

Martin Calloway
Managing Director
m.0481639027
e.martin@rbwgroup.com.au

Simon Calloway
Director
m.0429561384
e.simon@rbwgroup.com.au

Industry/Entity Type

Events

Requirements
Must have
• Under the Logo, we would like 'Western Australia'

```html
<!DOCTYPE html>
<html lang="en">
<head>
<meta charset="utf-8">
<title>Ridgeback Boring Works – Business Card</title>
<link href="https://fonts.googleapis.com/css2?family=Open+Sans:wght@400;600;700&display=swap" rel="stylesheet">
<style>
  :root {
    --brand-blue: #1b4f93;
    --brand-blue-dark: #123e7a;
    --brand-grey: #5f6266;
    --card-white: #f4f4f4;
    --canvas-bg: #e6e7e9;
    --text-white: #ffffff;
    --text-dark: #333333;
  }
  * { box-sizing: border-box; margin: 0; padding: 0; }
  html, body { width: 1200px; height: 880px; overflow: hidden; }
  body {
    background: var(--canvas-bg);
    font-family: "Open Sans", Arial, sans-serif;
    display: flex;
    align-items: center;
    justify-content: center;
    gap: 40px;
  }
  .card {
    width: 540px;
    height: 330px;
    position: relative;
    overflow: hidden;
    box-shadow: 0 6px 18px rgba(0,0,0,0.18);
  }

  /* Front */
  .card-front {
    background: linear-gradient(160deg, #2360a8 0%, var(--brand-blue) 45%, var(--brand-blue-dark) 100%);
    color: var(--text-white);
    display: flex;
    flex-direction: column;
    align-items: center;
    justify-content: center;
  }
  .brand-lockup { display: flex; align-items: center; gap: 14px; }
  .brand-mark { width: 22px; height: 22px; background: var(--text-white); }
  .brand-name {
    font-size: 32px;
    font-weight: 700;
    letter-spacing: 0.5px;
  }
  .brand-region {
    margin-top: 14px;
    font-size: 15px;
    letter-spacing: 9px;
    font-weight: 400;
  }
  .front-web {
    margin-top: 38px;
    font-size: 14px;
  }

  /* Back */
  .card-back { background: var(--card-white); }
  .back-brand {
    position: absolute;
    left: 44px;
    top: 60px;
    display: flex;
    align-items: center;
    gap: 12px;
    padding-bottom: 10px;
    border-bottom: 5px solid var(--brand-blue);
  }
  .back-brand .brand-mark { width: 18px; height: 18px; background: var(--brand-blue); }
  .back-brand .brand-name { font-size: 26px; color: var(--brand-blue); }
  .person {
    position: absolute;
    right: 48px;
    top: 168px;
    text-align: left;
  }
  .person-name {
    font-size: 22px;
    font-weight: 700;
    color: var(--brand-blue);
  }
  .person-role { font-size: 13px; color: var(--text-dark); }
  .contact-band {
    position: absolute;
    left: 0; right: 0; bottom: 0;
    height: 52px;
    background: var(--brand-blue);
    color: var(--text-white);
    display: flex;
    align-items: center;
    justify-content: space-between;
    padding: 0 26px;
    font-size: 13px;
  }
  .contact-item { display: flex; align-items: center; gap: 7px; }
  .contact-item svg { width: 14px; height: 14px; fill: var(--text-white); }
</style>
</head>
<body>

  <section class="card card-front">
    <div class="brand-lockup">
      <span class="brand-mark"></span>
      <span class="brand-name">Ridgeback Boring Works</span>
    </div>
    <p class="brand-region">Western Australia</p>
    <p class="front-web">www.rbwgroup.com.au</p>
  </section>

  <section class="card card-back">
    <div class="back-brand">
      <span class="brand-mark"></span>
      <span class="brand-name">Ridgeback Boring Works</span>
    </div>

    <div class="person">
      <p class="person-name">Simon Calloway</p>
      <p class="person-role">Director</p>
    </div>

    <div class="contact-band">
      <span class="contact-item">
        <svg viewBox="0 0 16 16" aria-hidden="true"><rect x="4" y="1" width="8" height="14" rx="1.5"/><rect x="5.5" y="3" width="5" height="8" fill="#1b4f93"/></svg>
        0429561384
      </span>
      <span class="contact-item">
        <svg viewBox="0 0 16 16" aria-hidden="true"><rect x="1" y="3" width="14" height="10" rx="1"/><path d="M1.5 3.5 L8 9 L14.5 3.5" stroke="#1b4f93" stroke-width="1.4" fill="none"/></svg>
        simon@rbwgroup.com.au
      </span>
      <span class="contact-item">www.rbwgroup.com.au</span>
    </div>
  </section>

</body>
</html>
```